Need Help having my business card stand out

I am the owner of Pine Ridge Canine Coaching and would like for my business cards to stand out. I have been trying to keep designing them myself but I can't get what I have in my head on the card. I will try my best to post templates that I like for inspirations. I want something unique but elegant. I don't want in to look cartoony or cheesy. It needs to pop in a pet shop but also in a coffee shop or gym.

Target Market(s)

Dog owners, Married ,No young kids Jr High school kids and up (maybe kids on the way) Executives, Stay at home moms/wives, Small business owners

Industry/Entity Type

Dog Training

Contact Information for Business Card

Trevor Holloway, 555-304-7162, info@pineridgecanine.example, www.pineridgecanine.example

Colors

Designer to choose colors to be used in the design.

Requirements
Must have
• my logo
Should not have
• Cursive lettering

```html
<!DOCTYPE html>
<html lang="en">
<head>
<meta charset="utf-8">
<title>Pine Ridge Canine Coaching – Business Card</title>
<link href="https://fonts.googleapis.com/css2?family=Tinos:wght@400;700&display=swap" rel="stylesheet">
<style>
  :root {
    --page-bg: #ecebe8;
    --card-grey-light: #6b6b6b;
    --card-grey-dark: #4a4a4a;
    --card-black: #1f1f1f;
    --ink-dark: #1a1a1a;
    --ink-light: #ffffff;
    --rule-light: rgba(255,255,255,0.85);
    --silhouette-dark: #262626;
    --silhouette-dark-2: #303030;
    --silhouette-light: #f4f4f4;
    --silhouette-light-2: #dcdcdc;
  }
  * { box-sizing: border-box; margin: 0; padding: 0; }
  html, body {
    width: 1200px; height: 1024px; overflow: hidden;
    background: var(--page-bg);
    font-family: "Tinos", "Times New Roman", serif;
  }
  .sheet {
    width: 1200px; height: 1024px;
    display: flex; flex-direction: column; align-items: center; justify-content: center;
    gap: 64px;
  }
  .card {
    position: relative;
    width: 700px; height: 400px;
    border-radius: 64px;
    overflow: hidden;
    box-shadow: 0 6px 16px rgba(0,0,0,0.18);
  }
  .card__rule {
    position: absolute; inset: 24px;
    border: 1.5px solid var(--rule-light);
    border-radius: 44px;
    pointer-events: none;
    z-index: 3;
  }

  /* Back */
  .card--back {
    background: linear-gradient(135deg, var(--card-grey-light), var(--card-grey-dark));
  }
  .back__mark {
    position: absolute; left: 140px; top: 110px;
    width: 420px; height: 180px;
    display: flex; align-items: center; gap: 24px;
  }
  .back__frame {
    flex: 1; height: 96px;
    border: 1px solid var(--ink-dark);
    display: flex; align-items: center; justify-content: center; gap: 12px;
    padding: 0 16px;
  }
  .brand-dot { width: 14px; height: 14px; background: var(--ink-dark); flex: none; }
  .back__name {
    color: var(--ink-dark); font-size: 21px; font-weight: 700; line-height: 1.2;
  }
  .back__dog {
    width: 100px; height: 170px; border-radius: 14px; flex: none;
    background: linear-gradient(180deg, var(--silhouette-dark-2), var(--silhouette-dark));
  }

  /* Front */
  .card--front { display: flex; }
  .front__identity {
    width: 50%;
    background: linear-gradient(90deg, var(--card-grey-light), var(--card-grey-dark));
    display: flex; flex-direction: column; align-items: center; justify-content: center;
    gap: 36px; padding: 10px 0 0 12px;
  }
  .front__brand {
    display: flex; align-items: center; gap: 12px;
    color: var(--ink-dark); font-size: 22px; font-weight: 700;
    line-height: 1.2;
  }
  .front__brand-name { white-space: nowrap; }
  .name-bar {
    display: flex; align-items: stretch;
    border: 1px solid var(--ink-dark);
    height: 36px;
  }
  .name-bar__initial {
    width: 44px; background: var(--ink-dark); color: var(--ink-light);
    display: flex; align-items: center; justify-content: center; font-size: 21px;
  }
  .name-bar__name {
    padding: 0 10px; display: flex; align-items: center; white-space: nowrap;
    color: var(--ink-dark); font-size: 20px; font-weight: 700; letter-spacing: 0.5px;
  }
  .front__contact {
    width: 50%; background: var(--card-black);
    display: flex; flex-direction: column; align-items: center;
    padding-top: 60px; gap: 24px;
  }
  .front__dog {
    width: 160px; height: 120px; border-radius: 14px;
    background: linear-gradient(160deg, var(--silhouette-light), var(--silhouette-light-2));
  }
  .contact-table {
    border-collapse: collapse; color: var(--ink-light); font-size: 17px;
  }
  .contact-table td {
    border: 1.5px solid var(--ink-light);
    height: 32px; padding: 0 6px;
  }
  .contact-table .icon { width: 44px; text-align: center; }
  .contact-table .icon svg { display: block; margin: 0 auto; }
  .contact-table .value { width: 240px; text-align: center; white-space: nowrap; }
</style>
</head>
<body>
<main class="sheet">

  <section class="card card--back" aria-label="Card back">
    <div class="card__rule"></div>
    <div class="back__mark">
      <div class="back__frame">
        <span class="brand-dot"></span>
        <span class="back__name">Pine Ridge Canine<br>Coaching</span>
      </div>
      <div class="back__dog" role="img" aria-label="Dark silhouette of a dog leaping upward"></div>
    </div>
  </section>

  <section class="card card--front" aria-label="Card front">
    <div class="card__rule"></div>
    <div class="front__identity">
      <div class="front__brand">
        <span class="brand-dot"></span>
        <span class="front__brand-name">Pine Ridge Canine<br>Coaching</span>
      </div>
      <div class="name-bar">
        <span class="name-bar__initial">H</span>
        <span class="name-bar__name">HOLLOWAY, Trevor</span>
      </div>
    </div>
    <div class="front__contact">
      <div class="front__dog" role="img" aria-label="White silhouette of a leaping dog"></div>
      <table class="contact-table">
        <tr>
          <td class="icon">
            <svg width="22" height="22" viewBox="0 0 24 24" aria-hidden="true"><path d="M6.6 3.5l3 3.2-1.8 2.3c1.2 2.6 3.2 4.6 5.8 5.8l2.3-1.8 3.2 3-1.9 3.2C10.4 19.6 4.4 13.6 3.4 6.8z" fill="none" stroke="#fff" stroke-width="1.8" stroke-linejoin="round"/></svg>
          </td>
          <td class="value">555-304-7162</td>
        </tr>
        <tr>
          <td class="icon">
            <svg width="24" height="24" viewBox="0 0 24 24" aria-hidden="true"><g fill="none" stroke="#fff" stroke-width="1.5"><circle cx="12" cy="12" r="9"/><ellipse cx="12" cy="12" rx="4" ry="9"/><path d="M3 12h18M5 7h14M5 17h14"/></g></svg>
          </td>
          <td class="value">www.pineridgecanine.example</td>
        </tr>
        <tr>
          <td class="icon">
            <svg width="26" height="20" viewBox="0 0 26 20" aria-hidden="true"><rect x="2" y="3" width="22" height="14" fill="#fff"/><path d="M2 3l11 8 11-8" fill="none" stroke="#1f1f1f" stroke-width="1.6"/></svg>
          </td>
          <td class="value">info@pineridgecanine.example</td>
        </tr>
      </table>
    </div>
  </section>

</main>
</body>
</html>
```